Business Cards for company that supports physicians that do medical research

Need to create a business card for Meridane Studies (www.valtrexstudies.example), a company devoted to supporting physicians who conduct medical research. The form of the card should match the message of research and information quest. I have provided the logo of the company as an uploaded file. Designs should be simple and slick aimed at very high end clients.

Target Market(s)

Medical doctors that are also researchers

Industry/Entity Type

Medical

Contact Information for Business Card

Should feature logo and fields for personal info:
Name/title
Phone /email

Font styles to use
Serif
Sans Serif

Requirements
Must have
• Meridane logo and fields for personal info:
• Name: Corwin Abbatelli
• Title: VP Research and Senior Analyst
• Phone: 555-203-7416
• email: info@valtrexstudies.example
Nice to have
• Interesting cards that I've seen:
• 1- all black/charcoal or very dark background
• 2- Plastic - semi-transparent
• 3- non-standard height-width ratios
• 4- Functional cards -- USB drive incorporated
Should not have
• Too busy; needs to stay very simple

```html
<!DOCTYPE html>
<html lang="en">
<head>
<meta charset="utf-8">
<title>Meridane Studies – Business Card</title>
<link rel="stylesheet" href="https://fonts.googleapis.com/css2?family=Raleway:wght@400;500;600;700&display=swap">
<style>
  :root {
    --page-bg: #e8e6e3;
    --card-dark: #1c1c1d;
    --card-mid: #2c2c2e;
    --accent-green: #4cc450;
    --accent-blue: #2b9de0;
    --text-light: #ececec;
    --text-muted: #c9c9c9;
  }
  html, body {
    margin: 0;
    padding: 0;
    width: 1200px;
    height: 900px;
    overflow: hidden;
    background: var(--page-bg);
  }
  .canvas {
    position: relative;
    width: 1200px;
    height: 900px;
  }
  .business-card {
    position: absolute;
    left: 150px;
    top: 193px;
    width: 900px;
    height: 514px;
    box-shadow: 0 18px 40px rgba(0,0,0,0.35);
  }
  .business-card svg {
    display: block;
    font-family: "Raleway", sans-serif;
  }
  .brand-name { fill: var(--text-light); font-weight: 600; font-size: 44px; letter-spacing: 1px; }
  .brand-mark { fill: var(--accent-green); }
  .person-first { fill: var(--text-light); font-weight: 600; font-size: 19px; }
  .person-last { fill: var(--accent-blue); font-weight: 600; font-size: 19px; }
  .person-title { fill: var(--text-muted); font-weight: 500; font-size: 15px; }
  .contact-text { fill: var(--text-light); font-weight: 500; font-size: 15px; }
  .contact-icon { fill: var(--accent-blue); }
  .icon-at { fill: var(--accent-blue); font-weight: 700; font-size: 26px; }
  .accent-line { fill: var(--accent-green); }
</style>
</head>
<body>
<main class="canvas">
  <section class="business-card">
    <svg width="900" height="514" viewBox="0 0 900 514" xmlns="http://www.w3.org/2000/svg">
      <defs>
        <linearGradient id="cardSurface" x1="0" y1="0" x2="1" y2="1">
          <stop offset="0" stop-color="#303032"/>
          <stop offset="1" stop-color="#1a1a1b"/>
        </linearGradient>
      </defs>

      <rect class="card-surface" role="img" aria-label="Dark carbon-fibre weave texture" width="900" height="514" fill="url(#cardSurface)"/>

      <g class="brand">
        <text class="brand-name" x="430" y="214" text-anchor="middle">Meridane Studies</text>
      </g>

      <g class="divider">
        <rect class="accent-line" x="0" y="247" width="820" height="8"/>
        <polygon class="accent-line" points="416,254 444,254 430,270"/>
        <rect class="accent-line" x="846" y="232" width="54" height="8"/>
      </g>

      <g class="person">
        <text x="430" y="305" text-anchor="middle">
          <tspan class="person-first">Firstname </tspan><tspan class="person-last">Lastname</tspan>
        </text>
        <text class="person-title" x="430" y="328" text-anchor="middle">Title</text>
      </g>

      <g class="contact-email">
        <text class="icon-at" x="690" y="296" text-anchor="middle">@</text>
        <text class="contact-text" x="690" y="322" text-anchor="middle">user@example.com</text>
      </g>

      <g class="contact-phone">
        <path class="contact-icon" transform="translate(318 380)" d="M2 4 C2 2 4 0 6 0 L9 0 L11 6 L8 8 C10 12 14 16 18 18 L20 15 L26 17 L26 20 C26 22 24 24 22 24 C10 24 2 16 2 4 Z"/>
        <text class="contact-text" x="330" y="428" text-anchor="middle">555.555.5555</text>
      </g>
    </svg>
  </section>
</main>
</body>
</html>
```